Window Cleaning Leaflet

Hi everyone,

I need a leaflet (couldn't find 'leaflet' as an option when begining this project - so one sided only) to send out to coastal properties in South side Melbourne. The Flyer is aimed at high net individuals, mummies, business people etc who own these properties who don't have time to clean the windows themselves (often multiple levels) and want their home looking fabulous in time for Christmas and NY's celebrations.

I would really love a new and original design for a window washing leaflet. something outside of the norm that 'pops' and makes people feel happy when they look at it.

I guess a point of differentiation is that I'm a female working in a mans industry so appeal to mothers looking for someone who is 'reliable, trustworthy and understanding of peoples needs'.

I have made an outline of what I would like included in the leaflet, so if you could please take a look, feel free to change things around, wording and layout etc. If you can make it sound more professional please do so.

I would like the colours to be 'happy' colours, maybe with a silly season theme?

Overall aesthetically pleasing is a must, I find most window cleaning leaflets fairly mundane and boring, please feel free to think outside the box. The more original the better.

Target Market(s)

People who own large Melbourne homes in affluent suburbs, mainly suburbs with a lot of large coastal properties. Generally owned by high net worth individuals who just don't have tme to clean the windows themselves due to their profession or hectic lifestyles but can afford to pay someone else to do it.

Industry/Entity Type

Window Cleaning

Requirements
Must have
• 1) The name of the business - Tilda’s Glass Gleam Services
• 2) The coupon special and all details attached:
• Small Homes (up to 12 windows) $120
• Medium Homes (up to 16 windows) $180
• Large Homes (up to 20 windows, 2 storeys) $240
• 20% discount
• *Discount applicable to first time customers only.
• *All services include fly screen, sill and tracks cleaned as well as cobweb removal.
• *Houses with more than 20 windows (or two levels) will have an immediate quote provided upon inspection of the property with 20% discount applied.
• *Tilda’s Glass Gleam Services are fully insured.
• 3) My contact number - 0418 263 905

```html
<!DOCTYPE html>
<html lang="en">
<head>
<meta charset="utf-8">
<title>Tilda’s Glass Gleam Services – Leaflet</title>
<link href="https://fonts.googleapis.com/css2?family=Lato:wght@300;400;700;900&display=swap" rel="stylesheet">
<style>
  :root{
    --page:#e9f1f7;
    --pink:#ee2a78;
    --pink-soft:#f7a3c4;
    --sky:#39a6dd;
    --sky-light:#bfe3f4;
    --navy:#1d3584;
    --white:#ffffff;
  }
  *{margin:0;padding:0;box-sizing:border-box;}
  html,body{width:1200px;height:1000px;overflow:hidden;background:var(--page);}
  body{position:relative;font-family:'Lato',sans-serif;}

  .leaflet{
    position:absolute;left:297px;top:56px;width:629px;height:892px;overflow:hidden;
    background:
      radial-gradient(ellipse 340px 230px at 78% 92%, rgba(255,255,255,.95), rgba(255,255,255,0) 70%),
      radial-gradient(ellipse 260px 160px at 45% 88%, rgba(255,255,255,.55), rgba(255,255,255,0) 70%),
      linear-gradient(180deg, var(--pink) 0%, #f0397f 38%, var(--pink-soft) 60%, var(--sky) 72%, #5fb8e4 88%, var(--sky-light) 100%);
  }

  .intro-list{
    position:absolute;left:36px;top:42px;width:470px;
    color:var(--white);font-weight:300;font-size:16.5px;line-height:22px;list-style:none;
  }
  .intro-list li{position:relative;padding-left:17px;}
  .intro-list li::before{content:"";position:absolute;left:2px;top:9px;width:5px;height:5px;border-radius:50%;background:var(--white);}

  .headline{
    position:absolute;left:49px;top:218px;width:220px;
    color:var(--white);font-weight:700;font-size:32px;line-height:40.6px;
  }
  .headline .accent{color:var(--navy);}

  .window-art{position:absolute;left:188px;top:172px;width:441px;height:456px;}

  .price-list{
    position:absolute;left:50px;top:599px;list-style:none;
    color:var(--navy);font-weight:400;font-size:24px;line-height:31px;
  }
  .price-list strong{font-weight:900;}

  .discount-badge{
    position:absolute;left:-30px;top:708px;width:304px;height:64px;border-radius:50%;
    background:var(--pink);transform:rotate(-4deg);
    display:flex;align-items:center;justify-content:center;padding-left:28px;
    color:var(--white);font-weight:900;font-size:28px;
  }

  .fine-print{
    position:absolute;left:48px;top:791px;width:268px;list-style:none;
    color:var(--navy);font-size:7.4px;line-height:9px;font-weight:400;
  }

  .brand-name{
    position:absolute;right:42px;top:720px;width:290px;text-align:right;
    color:var(--pink);font-weight:300;font-size:34px;line-height:38px;
  }

  .call-line{
    position:absolute;right:48px;top:832px;
    color:var(--navy);font-weight:300;font-size:30px;letter-spacing:.5px;white-space:nowrap;
  }
</style>
</head>
<body>
  <main class="leaflet">
    <ul class="intro-list">
      <li>Do you need your windows cleaned?</li>
      <li>Are you simply too busy as a hard working parent to do it yourself?</li>
      <li>Tilda understands and wants to help you - enjoy your home looking it’s best before Christmas and NY’s celebrations begin.</li>
      <li>We provide a reliable, professional service, ensuring that your home will sparkle.</li>
    </ul>

    <h1 class="headline">Call<br>Tilda<br><span class="accent">today</span><br>and take<br>advantage<br>of our<br>special<br>introductory<br>offer</h1>

    <svg class="window-art" viewBox="0 0 441 456" role="img" aria-label="Illustration of many overlapping tilted window frames with blue glass catching a sun flare">
      <defs>
        <linearGradient id="glass" x1="0" y1="0" x2="1" y2="1">
          <stop offset="0" stop-color="#c98ad0"/>
          <stop offset=".45" stop-color="#7da2e6"/>
          <stop offset="1" stop-color="#2f6fcf"/>
        </linearGradient>
      </defs>
      <polygon points="120,60 210,5 300,60 390,70 420,140 436,300 410,420 330,456 250,400 150,370 90,290 0,150 40,90" fill="url(#glass)" opacity=".85"/>
    </svg>

    <ul class="price-list">
      <li>Small Homes (up to 12 windows) <strong>$120</strong></li>
      <li>Medium Homes (up to 16 windows) <strong>$180</strong></li>
      <li>Large Homes (up to 20 windows, 2 storeys) <strong>$240</strong></li>
    </ul>

    <div class="discount-badge">20% discount</div>

    <ul class="fine-print">
      <li>*Discount applicable to first time customers only.</li>
      <li>*All services include fly screen, sill and tracks cleaned as well as cobweb removal.</li>
      <li>*Houses with more than 20 windows (or two levels) will have an immediate quote provided upon inspection of the property with 20% discount applied.</li>
      <li>*Tilda’s Glass Gleam Services are fully insured.</li>
    </ul>

    <p class="brand-name">Tilda’s Glass Gleam Services</p>

    <p class="call-line">CALL 0418 263 905</p>
  </main>
</body>
</html>
```